Fitness Centre/Personal Trainer Business Card

We need a business card design for a company based in Singapore called 'Vigor Summit'.

We are a team of Personal Trainers and we are planning to open our new training facility.

This design will also be printed/painted on the walls in our gym.

We are a new breed of personal trainers who take fitness seriously and holistically. We do not merely train our clients to be big and muscular.

We believe in wholeness. In our opinion, fitness should include: strength, speed, flexibility, mobility, stamina & agility. These are what we train for. Of course, nutrition/diet is key.

We use fitness tools such as kettlebells, QLV, Pylometric boxes, battling ropes, clubbells, medicine balls, bulgarian bags etc - functional and non-bulky tools.

I currently have a Facebook page 'Vigor Summit SG' which shows a logo of a kettlebell. But my business focus has since changed.

Services provided:
- Kettlebell Sport Preparation
- Calisthenics Training
- Corrective Exercises
- Sports Strength & Conditioning
- 28 days Weight Loss Program
- Myofascial Rehab Therapy
- Sports/Thai Massage

Main colors for the design should be BLACK & YELLOW. We envision a design which is able to protray the holistic view we take on fitness. Also it should somewhat appeal to the ladies and not intimidate them.

Target Market(s)

People between 18-35 years old. Students and working class alike.

Industry/Entity Type

Training

Requirements
Must have
• Name: Marcus Oleander Pryce
Fitness Coach
Corrective Exercise Specialist
M: +65 9372 6058
E: marcus@sgvigorsummit-example.com

Double-sided please.
Nice to have
• "What is your vigor summit?"

```html
<!DOCTYPE html>
<html lang="en">
<head>
<meta charset="utf-8">
<title>Vigor Summit — Business Card</title>
<link rel="stylesheet" href="https://fonts.googleapis.com/css2?family=Squada+One&display=swap">
<style>
  :root {
    --ink: #0b0b0b;
    --yellow: #f5e11a;
    --white: #f4f4f4;
    --page: #e9e7e2;
    --photo-light: #6d6d6d;
    --photo-dark: #141414;
  }
  * { box-sizing: border-box; margin: 0; padding: 0; }
  html, body { width: 1200px; height: 1024px; overflow: hidden; }
  body {
    background: var(--page);
    font-family: "Squada One", "Arial Narrow", sans-serif;
    display: flex; flex-direction: column; align-items: center; justify-content: center;
    gap: 24px;
  }
  .card {
    position: relative; width: 840px; height: 480px;
    background: var(--ink); color: var(--white); overflow: hidden;
    box-shadow: 0 6px 18px rgba(0,0,0,.25);
  }
  .card svg.art { position: absolute; inset: 0; }
  .front .content { position: absolute; left: 420px; top: 60px; width: 390px; }
  .brand-title { font-size: 68px; line-height: 1; letter-spacing: 1px; text-transform: uppercase; }
  .brand-title .accent { color: var(--yellow); }
  .services-label { margin-top: 16px; color: var(--yellow); font-size: 20px; font-variant: small-caps; }
  .services { list-style: none; margin-top: 4px; font-size: 19px; line-height: 1.25; font-variant: small-caps; }
  .services li::before { content: "• "; color: var(--yellow); }
  .tagline { margin-top: 34px; font-size: 32px; line-height: 1.05; text-transform: uppercase; text-align: right; }
  .tagline .accent { color: var(--yellow); }
  .tagline-rule { display: flex; align-items: center; justify-content: flex-end; gap: 12px; }
  .tagline-rule::before { content: ""; flex: 1; height: 2px; background: var(--yellow); }

  .back .contact { position: absolute; right: 56px; top: 70px; text-align: right; }
  .person-name { color: var(--yellow); font-size: 46px; text-transform: uppercase; line-height: 1; }
  .person-role { font-size: 26px; font-variant: small-caps; margin-top: 4px; }
  .contact-lines { margin-top: 26px; font-size: 22px; line-height: 1.35; font-variant: small-caps; }
  .contact-lines b { color: var(--yellow); font-weight: 400; }
  .back .wordmark { position: absolute; right: 56px; bottom: 56px; text-align: right; }
  .wordmark-name { font-size: 64px; text-transform: uppercase; line-height: 1; color: var(--white); }
  .wordmark-site { font-size: 24px; color: var(--yellow); text-transform: uppercase; margin-top: 6px; }
</style>
</head>
<body>

<section class="card front" aria-label="Card front">
  <svg class="art" width="840" height="480" viewBox="0 0 840 480" aria-hidden="false">
    <defs>
      <radialGradient id="photoTone" cx="45%" cy="50%" r="60%">
        <stop offset="0%" stop-color="var(--photo-light)"/>
        <stop offset="100%" stop-color="var(--photo-dark)"/>
      </radialGradient>
      <linearGradient id="photoFade" x1="0" x2="1">
        <stop offset="70%" stop-color="#0b0b0b" stop-opacity="0"/>
        <stop offset="100%" stop-color="#0b0b0b" stop-opacity="1"/>
      </linearGradient>
    </defs>
    <g role="img" aria-label="Black and white photo of an athlete lifting a dumbbell">
      <rect x="0" y="60" width="420" height="400" fill="url(#photoTone)"/>
      <rect x="0" y="60" width="420" height="400" fill="url(#photoFade)"/>
    </g>
    <polygon class="jag-top" fill="var(--yellow)"
      points="0,0 330,0 300,40 270,28 230,90 190,62 150,120 110,96 70,150 0,165"/>
    <polygon class="jag-bottom" fill="var(--yellow)"
      points="0,330 60,300 100,340 150,296 200,356 250,318 300,400 330,380 380,480 0,480"/>
  </svg>
  <div class="content">
    <h1 class="brand-title"><span class="accent">Vigor</span> Summit</h1>
    <p class="services-label">Services provided:</p>
    <ul class="services">
      <li>Kettlebell Sport Preparation</li>
      <li>Calisthenics Training</li>
      <li>Corrective Exercises</li>
      <li>Sports Strength &amp; Conditioning</li>
      <li>28 Days Weight Loss Program</li>
      <li>Myofascial Rehab Therapy</li>
      <li>Sports/Thai Massage</li>
    </ul>
    <p class="tagline">What is your vigor<br><span class="tagline-rule"><span class="accent">summit?</span></span></p>
  </div>
</section>

<section class="card back" aria-label="Card back">
  <svg class="art" width="840" height="480" viewBox="0 0 840 480" aria-hidden="true">
    <polygon fill="var(--yellow)"
      points="0,0 220,0 190,60 160,44 130,120 100,96 70,190 40,170 0,260"/>
  </svg>
  <div class="contact">
    <h2 class="person-name">Marcus Oleander Pryce</h2>
    <p class="person-role">Fitness Coach</p>
    <p class="contact-lines">
      Corrective Exercise Specialist<br>
      <b>M:</b> +65 9372 6058<br>
      <b>E:</b> marcus@sgvigorsummit-example.com
    </p>
  </div>
  <div class="wordmark">
    <p class="wordmark-name">Vigor Summit</p>
    <p class="wordmark-site">sgvigorsummit-example.com</p>
  </div>
</section>

</body>
</html>
```